Building company business card

Design and print business cards for BRENTHOLM PTY LTD.
A residantial homes building company.
Mark Lantern already designed the company Logo.

```html
<!DOCTYPE html>
<html lang="en">
<head>
<meta charset="utf-8">
<title>BRENTHOLM PTY LTD – Business Card</title>
<link href="https://fonts.googleapis.com/css2?family=Arimo:wght@400;700&display=swap" rel="stylesheet">
<style>
  :root {
    --backdrop: #3b322d;
    --navy: #232a6b;
    --gold: #c9942f;
    --gold-light: #e8bd5f;
    --white: #ffffff;
    --ink: #1b1b1b;
  }
  * { margin: 0; padding: 0; box-sizing: border-box; }
  html, body { width: 1200px; height: 822px; overflow: hidden; }
  body {
    background: var(--backdrop);
    font-family: "Arimo", Arial, sans-serif;
    position: relative;
  }
  .card {
    position: absolute;
    width: 520px;
    height: 317px;
    border-radius: 18px;
    overflow: hidden;
    box-shadow: 0 14px 30px rgba(0,0,0,.45);
  }
  .card-back {
    left: 60px; top: 70px;
    background: var(--navy);
    display: flex; align-items: center; justify-content: center;
  }
  .back-brand {
    color: var(--white);
    font-weight: 700;
    font-size: 50px;
    letter-spacing: 1px;
  }
  .card-front {
    left: 620px; top: 430px;
    background: var(--white);
  }
  .wave { position: absolute; left: 0; top: 0; width: 520px; height: 317px; }
  .front-brand {
    position: absolute;
    left: 30px; top: 125px;
    width: 210px;
    color: var(--navy);
    font-weight: 700;
    font-size: 27px;
    line-height: 1.1;
    display: flex; align-items: center; gap: 10px;
  }
  .brand-square {
    width: 16px; height: 16px;
    background: var(--gold);
    flex: none;
  }
  .divider {
    position: absolute;
    left: 250px; top: 52px;
    width: 1px; height: 150px;
    background: var(--navy);
  }
  .contact {
    position: absolute;
    left: 268px; top: 46px;
    color: var(--ink);
    font-size: 12.5px;
    line-height: 1.35;
  }
  .contact-name {
    color: var(--navy);
    font-weight: 700;
    font-size: 15px;
  }
  .contact-role { font-size: 13.5px; margin-bottom: 8px; }
  .contact-address { margin-bottom: 6px; }
  .contact-line { display: flex; align-items: center; gap: 6px; }
  .contact-line svg { width: 11px; height: 11px; flex: none; }
  .registration {
    position: absolute;
    right: 22px; bottom: 24px;
    color: var(--white);
    font-size: 12px;
    letter-spacing: .3px;
  }
  .registration .sep { color: var(--gold-light); margin: 0 4px; }
</style>
</head>
<body>

  <section class="card card-back">
    <div class="back-brand">BRENTHOLM</div>
  </section>

  <section class="card card-front">
    <svg class="wave" viewBox="0 0 520 317" aria-hidden="true">
      <path d="M0 272 C150 302 320 272 420 238 C470 221 500 216 520 216 L520 317 L0 317 Z" fill="var(--navy)"/>
      <path d="M0 263 C150 293 320 263 420 229 C470 212 500 207 520 207" fill="none" stroke="var(--gold)" stroke-width="4"/>
    </svg>

    <div class="front-brand"><span class="brand-square"></span><span>BRENTHOLM PTY LTD</span></div>
    <div class="divider"></div>

    <div class="contact">
      <div class="contact-name">DORIAN (Dee) CASTELL</div>
      <div class="contact-role">Director</div>
      <div class="contact-address">PO Box 274<br>Fernlea North Vic 3190</div>
      <div class="contact-line">
        <svg viewBox="0 0 12 12"><rect x="3" y="0.5" width="6" height="11" rx="1" fill="none" stroke="var(--gold)" stroke-width="1.2"/></svg>
        0412 555 203
      </div>
      <div class="contact-line">
        <svg viewBox="0 0 12 12"><path d="M2 1 L4.5 1 L5.5 3.5 L4 4.5 C5 6.5 5.5 7 7.5 8 L8.5 6.5 L11 7.5 L11 10 C6 11 1 6 2 1 Z" fill="var(--gold)"/></svg>
        0433 555 918
      </div>
      <div class="contact-line">
        <svg viewBox="0 0 12 12"><rect x="0.5" y="2" width="11" height="8" fill="var(--gold)"/><path d="M0.5 2 L6 6.5 L11.5 2" fill="none" stroke="var(--white)" stroke-width="1"/></svg>
        dc@brentholm-pl.com
      </div>
      <div class="contact-line">
        <svg viewBox="0 0 12 12"><circle cx="6" cy="6" r="5.2" fill="none" stroke="var(--gold)" stroke-width="1.2"/><path d="M1 6 H11 M6 1 C3 4 3 8 6 11 M6 1 C9 4 9 8 6 11" fill="none" stroke="var(--gold)" stroke-width=".8"/></svg>
        www.brentholm-pl.com
      </div>
    </div>

    <div class="registration">ABN- 48 201 556 907<span class="sep">|</span>CDB-U 51846</div>
  </section>

</body>
</html>
```